HiItsJonBrell.com needs a modern, eye-catching business card design

My name is Jon Brell and I own a video training (software development industry) website. I need a business card design that is eye catching for when I travel to conferences or do seminars. I would prefer something simple but bold. Something along the lines of this: https://pixvaultstatic.example/gallery_img/530172/44018/44018_9917302_530172_image.jpg

Note that I do not have a specific logo, but I do have an caricature I use on my site of myself. I've not attached it because I'm not really a fan of having it on my business cards. I would prefer lettering instead of an image. You can go to my website (https://hiitsjonbrell.com) for inspiration.

I want to add the following information on my card (the order of these, their size, and their casing is up to you):

Jon Brell
jon@HiItsJonBrell.com
@HiItsJonBrell
HiItsJonBrell.com
vidsharehub.example/HiItsJonBrell

I would also like to have somewhere on the card a small ad that says "Get a free course at https://HiItsJonBrell.com/FreeCourse". Feel free to play with that wording or layout if you need. I would prefer this text to be at the bottom of the card and subtle. Some small eye-catching thing might be ok but nothing huge or garish.

I plan on printing this card at pressquill.example (https://www.pressquill.example/us/design-guidelines/business-cards.html). I would like it to be the standard size (3.66" x 2.16"). I would prefer rounded corners and horizontal orientation. This is a two-side design. I would prefer the side with all of the information be primarily white but I like color text (again, flexible on that). On the front side, I like simple. Maybe just HiItsJonBrell.com (casing on that is up to you - whatever looks and reads the best - that goes for all of the casing). As for font choices, I prefer a modern, clean font. For example, Open Sans Light can be a nice option.

Website Info (might be helpful for the card):
Color Palette

Darkest blue - #263246
Alternate blue - #2F4E6A
Light blue - #2A98C3
Orange - #FF6201
White - #FFFFFF

Font for Jon Brell Logo

Jellyka Estryas Handwriting
http://www.typecrate.example/jellyka_estryas_handwriting.font

Fonts for Site Content and VidShare Thumbnails

Lovelo (bold title font)
http://www.glyphmill.example/lovelo-font/

Open Sans (body font)
http://www.letterbarn.example/fonts/open-sans

Industry/Entity Type

Software Development

Contact Information for Business Card

Jon Brell
jon@HiItsJonBrell.com
@HiItsJonBrell
HiItsJonBrell.com
vidsharehub.example/HiItsJonBrell

Get a free course at https://HiItsJonBrell.com/FreeCourse

Colors

Designer to choose colors to be used in the design.

Requirements
Nice to have
• Modern color - maybe primarily a color on the front and then that color as an accent on the back.
Should not have
• Lots of colors - I LOVE color but do not want a rainbow of colors on the card.

```html
<!DOCTYPE html>
<html lang="en">
<head>
<meta charset="utf-8">
<title>Jon Brell – Business Card</title>
<link rel="stylesheet" href="https://fonts.googleapis.com/css2?family=Open+Sans:wght@300;400;600;700;800&display=swap">
<style>
  :root {
    --stage: #e6e7ea;
    --card-navy: #1c2639;
    --divider: #151d2c;
    --icon-box: #263246;
    --accent-blue: #2a98c3;
    --ink-dark: #0f1620;
    --white: #ffffff;
  }
  * { margin: 0; padding: 0; box-sizing: border-box; }
  html, body { width: 1200px; height: 1000px; overflow: hidden; }
  body {
    position: relative;
    background: var(--stage);
    font-family: "Open Sans", Arial, sans-serif;
    color: var(--white);
  }
  .card {
    position: absolute;
    left: 228px;
    width: 742px;
    background: var(--card-navy);
    box-shadow: 0 6px 18px rgba(0,0,0,0.35);
    overflow: hidden;
  }
  .card--info { top: 58px; height: 427px; }
  .card--front { top: 513px; height: 424px; }

  /* Info side */
  .info-divider {
    position: absolute;
    left: 345px; top: 0;
    width: 3px; height: 373px;
    background: var(--divider);
  }
  .name-mark {
    position: absolute;
    font-weight: 300;
    color: var(--white);
    white-space: nowrap;
  }
  .card--info .name-mark {
    left: 44px; top: 150px;
    font-size: 56px;
    letter-spacing: 1px;
  }
  .contact-list { list-style: none; }
  .contact-item {
    position: absolute;
    left: 347px;
    right: 16px;
    display: flex;
    align-items: center;
    height: 46px;
  }
  .contact-item:nth-child(1) { top: 57px; }
  .contact-item:nth-child(2) { top: 140px; }
  .contact-item:nth-child(3) { top: 216px; }
  .contact-item:nth-child(4) { top: 290px; }
  .contact-icon {
    flex: 0 0 46px;
    width: 46px; height: 46px;
    background: var(--icon-box);
    box-shadow: 2px 2px 4px rgba(0,0,0,0.5);
    display: flex; align-items: center; justify-content: center;
  }
  .contact-text {
    margin-left: 17px;
    font-size: 21px;
    font-weight: 400;
    white-space: nowrap;
  }
  .contact-text--long {
    font-size: 16.5px;
    letter-spacing: -0.1px;
  }
  .video-square {
    width: 24px; height: 18px;
    background: var(--accent-blue);
    border-radius: 3px;
  }
  .promo-band {
    position: absolute;
    left: 0; bottom: 0;
    width: 100%; height: 54px;
    background: var(--accent-blue);
    display: flex; align-items: center; justify-content: center;
    font-size: 19px;
    font-weight: 700;
    color: var(--ink-dark);
    white-space: nowrap;
  }
  .promo-band .promo-link { color: var(--white); margin-left: 6px; }

  /* Front side */
  .card--front .name-mark {
    left: 0; width: 100%;
    top: 95px;
    text-align: center;
    font-size: 112px;
    letter-spacing: 2px;
  }
  .site-rule {
    position: absolute;
    height: 15px;
    background: var(--accent-blue);
    top: 328px;
  }
  .site-rule--left { left: 0; width: 226px; }
  .site-rule--right { right: 0; width: 226px; }
  .site-url {
    position: absolute;
    top: 320px; left: 0; width: 100%;
    text-align: center;
    font-size: 20px;
    font-weight: 700;
    color: var(--accent-blue);
  }
  .base-rule {
    position: absolute;
    top: 357px; left: 0;
    width: 100%; height: 4px;
    background: var(--accent-blue);
  }
</style>
</head>
<body>

<section class="card card--info" aria-label="Contact side">
  <div class="info-divider"></div>
  <div class="name-mark">Jon Brell</div>
  <ul class="contact-list">
    <li class="contact-item">
      <span class="contact-icon">
        <svg width="36" height="36" viewBox="0 0 36 36" fill="none" stroke="#2a98c3" stroke-width="2.4">
          <circle cx="18" cy="18" r="15"/>
          <ellipse cx="18" cy="18" rx="6.5" ry="15"/>
          <line x1="3" y1="18" x2="33" y2="18"/>
          <line x1="18" y1="3" x2="18" y2="33"/>
          <path d="M6 10h24M6 26h24"/>
        </svg>
      </span>
      <span class="contact-text">HiItsJonBrell.com</span>
    </li>
    <li class="contact-item">
      <span class="contact-icon">
        <svg width="36" height="26" viewBox="0 0 36 26">
          <rect x="1" y="1" width="34" height="24" fill="#2a98c3"/>
          <path d="M1 1L18 15L35 1M1 25L13 11M35 25L23 11" fill="none" stroke="#263246" stroke-width="2"/>
        </svg>
      </span>
      <span class="contact-text">@HiItsJonBrell</span>
    </li>
    <li class="contact-item">
      <span class="contact-icon">
        <svg width="36" height="26" viewBox="0 0 36 26">
          <rect x="1" y="1" width="34" height="24" fill="#2a98c3"/>
          <path d="M1 1L18 15L35 1M1 25L13 11M35 25L23 11" fill="none" stroke="#263246" stroke-width="2"/>
        </svg>
      </span>
      <span class="contact-text">jon@HiItsJonBrell.com</span>
    </li>
    <li class="contact-item">
      <span class="contact-icon"><span class="video-square"></span></span>
      <span class="contact-text contact-text--long">vidsharehub.example/HiItsJonBrell</span>
    </li>
  </ul>
  <div class="promo-band">Get a FREE COURSE at <span class="promo-link">https://HiItsJonBrell.com/FreeCourse</span></div>
</section>

<section class="card card--front" aria-label="Name side">
  <div class="name-mark">Jon Brell</div>
  <div class="site-rule site-rule--left"></div>
  <div class="site-rule site-rule--right"></div>
  <div class="site-url">www.HiItsJonBrell.com</div>
  <div class="base-rule"></div>
</section>

</body>
</html>
```